Hair spray product label design

I've developed a daily conditioning hair spray that all women can use. The formula focuses on maintaining frizz, moisturizing, conditioning, protecting heat damage, and detangles. The product will be distributed to hair salons, internet, and beauty shops. The spray will be sold at approximately $10.00. I need to have the label designed according to those specifics. I've attached sample photos of products I sell in my shop for you to see. I need a design that will grab customers' attention and fall in love with.

Target Market(s)

age group 25-60, female.

Industry/Entity Type

Hair Care Product

Font styles to use
Sans Serif

Colors
0792cd
33a6d7
ec1f27
f04a50
b868aa
d3a5cc

Requirements
Must have
• The clear PP film will be used on a white non-transparent bottle. Letters and pictures must be visible. A barcode area must be reserved. Words must be able to be edited.
Nice to have
• I would welcome any suggestions and new ideas for the label.
Should not have
• feel of complicated, cheap, old, faded, too much color.

```html
<!DOCTYPE html>
<html lang="en">
<head>
<meta charset="utf-8">
<title>Lumera Thermal Protectant Mist Label</title>
<link href="https://fonts.googleapis.com/css2?family=Didact+Gothic&family=Questrial&family=Arimo:wght@400;700&display=swap" rel="stylesheet">
<style>
  :root {
    --stage: #efefef;
    --label-white: #ffffff;
    --mist-blue: #bfe0ef;
    --mist-blue-deep: #a9d3e6;
    --ink: #2b2b2b;
    --soft-grey: #8a8f93;
    --rule: #9fb3bd;
    --pill: #3a3a3a;
    --accent-blue: #33a6d7;
    --accent-red: #ec1f27;
    --accent-violet: #b868aa;
  }
  html, body { margin: 0; padding: 0; overflow: hidden; }
  body {
    width: 1200px; height: 1200px;
    background: radial-gradient(circle at 50% 45%, #fafafa 0%, var(--stage) 75%);
    display: flex; align-items: center; justify-content: center;
    font-family: "Arimo", Arial, sans-serif;
  }
  .label {
    position: relative;
    width: 1100px; height: 640px;
    background: var(--label-white);
    box-shadow: 0 10px 30px rgba(0,0,0,0.08);
    overflow: hidden;
  }
  .label__art { position: absolute; inset: 0; }
  .panel { position: absolute; top: 0; height: 100%; }
  .panel--front { left: 0; width: 520px; }
  .panel--back { left: 540px; width: 540px; }

  .brand {
    font-family: "Questrial", sans-serif;
    font-size: 58px; color: var(--ink); letter-spacing: 1px;
    margin: 0; line-height: 1;
  }
  .brand sup { font-size: 16px; vertical-align: top; margin-left: 4px; }
  .subtitle {
    font-family: "Didact Gothic", sans-serif;
    color: var(--soft-grey); font-size: 23px; line-height: 1.25; margin: 8px 0 0;
  }
  .panel--front .masthead { position: absolute; top: 56px; left: 0; width: 100%; text-align: center; }
  .hero-art {
    position: absolute; left: 170px; top: 196px; width: 180px; height: 236px;
    background: linear-gradient(160deg, rgba(51,166,215,0.25), rgba(184,104,170,0.25) 55%, rgba(236,31,39,0.2));
    border-radius: 40px;
  }
  .claims {
    position: absolute; top: 448px; left: 0; width: 100%; text-align: center;
    font-family: "Arimo", sans-serif; color: var(--ink);
  }
  .claims__item {
    display: block; width: 180px; margin: 0 auto; padding: 3px 0 4px;
    border-bottom: 1px solid var(--rule); font-size: 16px;
  }
  .claims__hair { font-size: 16px; margin-top: 6px; line-height: 1.15; }
  .volume {
    display: inline-block; margin-top: 12px; padding: 3px 14px;
    background: var(--pill); color: #fff; border-radius: 12px; font-size: 15px;
  }

  .panel--back .masthead { position: absolute; top: 44px; left: 30px; }
  .panel--back .brand { font-size: 44px; }
  .panel--back .subtitle { font-size: 18px; }
  .tagline { font-size: 12px; color: var(--ink); margin: 8px 0 0; }
  .back-copy {
    position: absolute; top: 190px; left: 30px; width: 380px;
    font-size: 11px; color: var(--ink); line-height: 1.35;
  }
  .back-copy .lede { font-weight: 700; font-size: 13px; margin: 0 0 8px; }
  .benefits { margin: 0 0 8px; padding-left: 14px; }
  .back-copy h3 { font-size: 12px; margin: 6px 0 2px; }
  .back-copy p { margin: 0 0 6px; }
  .fineprint { font-size: 8.5px; text-transform: uppercase; line-height: 1.3; }
  .distributor { font-size: 9.5px; margin-top: 6px; }
  .barcode-area {
    position: absolute; left: 440px; top: 420px; width: 68px; height: 130px;
    border: 1px solid #9a9a9a; background: #fff;
  }
  .cruelty-free {
    position: absolute; left: 320px; top: 548px; width: 52px; height: 52px;
    border-radius: 50%; background: #222;
  }
</style>
</head>
<body>
  <main class="label">
    <svg class="label__art" width="1100" height="640" viewBox="0 0 1100 640" aria-hidden="true">
      <defs>
        <clipPath id="front-band"><rect x="0" y="40" width="520" height="580"/></clipPath>
      </defs>
      <rect x="0" y="40" width="520" height="580" fill="var(--mist-blue)"/>
      <g clip-path="url(#front-band)" fill="var(--mist-blue-deep)" opacity="0.75">
        <circle cx="150" cy="310" r="150"/>
        <circle cx="390" cy="330" r="150"/>
        <circle cx="250" cy="570" r="190"/>
      </g>
      <circle cx="1110" cy="430" r="150" fill="var(--mist-blue)"/>
    </svg>

    <section class="panel panel--front">
      <header class="masthead">
        <h1 class="brand">Lumera<sup>™</sup></h1>
        <p class="subtitle">Natural Styling<br>Thermal Protectant Mist</p>
      </header>
      <div class="hero-art" role="img" aria-label="Illustration of a flowing hair strand with colourful bubbles"></div>
      <div class="claims">
        <span class="claims__item">Daily Styling Spray</span>
        <span class="claims__item">Lightweight</span>
        <span class="claims__item">Thermal Protection</span>
        <div class="claims__hair">For Straight, Virgin,<br>Processed, Curly &amp; Wavy Hair</div>
        <span class="volume">8 FL oz / 237mL</span>
      </div>
    </section>

    <section class="panel panel--back">
      <header class="masthead">
        <h2 class="brand">Lumera<sup>™</sup></h2>
        <p class="subtitle">Natural Styling<br>Thermal Protectant Mist</p>
        <p class="tagline">Daily Styling Spray | Oil Free, Lightweight | For all Hair Types</p>
      </header>
      <div class="back-copy">
        <p class="lede">A cocktail of lightweight thickening elements pumps up the volume and shine, while flexible styling agents grip skinny strands with clean hold.</p>
        <ul class="benefits">
          <li>Prevents Frizz &amp; Damage to Cuticle</li>
          <li>Superior Slip for Wet/Dry combing</li>
          <li>Detangles</li>
          <li>Silky Smooth Finish</li>
          <li>Reduce Static</li>
          <li>Thermal Protection</li>
          <li>Superb Conditioning</li>
        </ul>
        <h3>Directions:</h3>
        <p>Do not rinse. Spray to clean, damp hair and comb through evenly. Style as usual.</p>
        <p class="fineprint"><strong>Ingredients:</strong> Water (Aqua, Eau), Cetyl Triethylmonium Dimethicone PEG-8 Succinate, Cetrimonium Methosulfate, Cetearyl Alcohol, Behentrimonium Methosulfate, Cetyl Alcohol, Butylene Glycol, Ethylhexylglycerin, Phenoxyethanol, Polysorbate 20, Fragrance</p>
        <p class="fineprint"><strong>Warning:</strong> Keep away from flame and high heat. Do not smoke during application and until hair is fully dry. Avoid contact with eyes and damaged skin. If eye contact occurs, rinse thoroughly. If eye irritation persists, contact a physician. External use only. If ingested, contact a physician or poison control immediately. Keep out of reach of children.</p>
        <p class="distributor">Distributed by Harbor Crest Beauty LLC.<br>Made in the USA<br><strong>www.lumerabeauty.com</strong></p>
      </div>
      <div class="cruelty-free" aria-hidden="true"></div>
      <div class="barcode-area" aria-label="Reserved barcode area"></div>
    </section>
  </main>
</body>
</html>
```